Landing page for a sports website

we have a sports tracking and management website and require a web site.
the site should have the ability to have 2 options for selection the first being a competitions portal the other a club portal there should be a about us page and a contact us page
the site should be dynamic and vibrant and be easily recognisable as a multiple sports page
we also have www.velorinote.com and would like it to compliment that site
i would like to have some form of animation regarding sports occur when you click the login option if that is possible
the site is www.vlnsports.com and I have attached the logo in both 3d and standard
we also require a design several templates for information pages please see www.tallyhusk.com as an example of how it should look but with a sports theme
Target Market(s)
This will be used for primarily team based sports
Industry/Entity Type
Management
Number of Pages Required
3 page
Requirements
Must have
- the ability to change the logo and names of the site
- i.e. from vlnsports to vlnschools at a later date

```html
<!DOCTYPE html>
<html lang="en">
<head>
<meta charset="utf-8">
<title>VLN Sports</title>
<link rel="stylesheet" href="https://fonts.googleapis.com/css2?family=Open+Sans:wght@400;600&family=Roboto+Slab:wght@500&display=swap">
<style>
  :root {
    --header-top: #1c1c1c;
    --header-bottom: #0b0b0b;
    --plate-light: #222222;
    --plate-dark: #0e0e0e;
    --footer-bg: #050505;
    --orange-light: #e27a46;
    --orange-dark: #a9471d;
    --blue-light: #13a8dc;
    --blue-dark: #0a769f;
    --brand-blue: #2aa9d9;
    --link-grey: #a9a9a9;
    --copy-grey: #8a8a8a;
    --divider: #555555;
    --white: #ffffff;
  }
  * { margin: 0; padding: 0; box-sizing: border-box; }
  html, body { width: 1200px; height: 1000px; overflow: hidden; background: var(--footer-bg); }
  .page { position: relative; width: 1200px; height: 1000px; font-family: "Open Sans", Arial, sans-serif; }

  .site-header {
    position: absolute; left: 0; top: 0; width: 1200px; height: 268px;
    background: linear-gradient(to bottom, var(--header-top), var(--header-bottom));
    border-bottom: 1px solid #2a2a2a;
  }
  .brand {
    position: absolute; left: 0; top: 100px; width: 1200px;
    display: flex; justify-content: center; align-items: center; gap: 18px;
  }
  .brand-mark { width: 40px; height: 40px; border-radius: 50%; background: var(--brand-blue); }
  .brand-name {
    font-family: "Roboto Slab", Georgia, serif; font-weight: 500;
    font-size: 64px; line-height: 80px; color: var(--brand-blue); letter-spacing: 1px;
  }

  .hero {
    position: absolute; left: 0; top: 269px; width: 1200px; height: 661px;
    background:
      radial-gradient(ellipse at 50% 30%, var(--plate-light) 0%, var(--plate-dark) 75%);
    box-shadow: inset 0 14px 20px rgba(0,0,0,0.7), inset 0 -14px 20px rgba(0,0,0,0.6);
  }
  .portal {
    position: absolute; top: 201px; width: 295px; height: 75px;
    display: flex; align-items: center; justify-content: center;
    font-family: "Roboto Slab", Georgia, serif; font-weight: 500;
    font-size: 25px; letter-spacing: 1px; color: var(--white);
    text-decoration: none; box-shadow: 0 6px 14px rgba(0,0,0,0.6);
  }
  .portal-competitions { left: 262px; background: linear-gradient(to bottom, var(--orange-light), var(--orange-dark)); }
  .portal-club { left: 648px; background: linear-gradient(to bottom, var(--blue-light), var(--blue-dark)); }

  .footer-nav {
    position: absolute; top: 455px; left: 0; width: 1200px;
    display: flex; justify-content: center; align-items: center;
  }
  .footer-nav a { color: var(--link-grey); text-decoration: none; font-size: 14px; }
  .footer-nav .about { margin-right: 33px; margin-left: -8px; }
  .footer-nav .divider { width: 1px; height: 33px; background: var(--divider); }
  .footer-nav .contact { margin-left: 30px; }

  .social {
    position: absolute; top: 523px; left: 0; width: 1200px;
    display: flex; justify-content: center; align-items: center; gap: 15px;
    color: var(--link-grey); font-size: 14px;
  }
  .social-label { margin-right: 0; }
  .social-icon { width: 19px; height: 19px; display: block; }
  .social-icon.one { background: #3b5ca0; }
  .social-icon.two { background: #35aadf; border-radius: 50%; }

  .site-footer {
    position: absolute; left: 0; top: 930px; width: 1200px; height: 70px;
    background: var(--footer-bg); border-top: 1px solid #1c1c1c;
    display: flex; justify-content: center; align-items: center;
    color: var(--copy-grey); font-size: 11px; letter-spacing: 0.3px;
  }
</style>
</head>
<body>
<div class="page">
  <header class="site-header">
    <div class="brand">
      <span class="brand-mark"></span>
      <span class="brand-name">VLN Sports</span>
    </div>
  </header>

  <main class="hero" role="img" aria-label="Dark diamond-plate metal texture background">
    <a class="portal portal-competitions" href="#">COMPETITIONS</a>
    <a class="portal portal-club" href="#">CLUB</a>

    <nav class="footer-nav">
      <a class="about" href="#">About VLN</a>
      <span class="divider"></span>
      <a class="contact" href="#">Get in Touch</a>
    </nav>

    <div class="social">
      <span class="social-label">Follow us on</span>
      <a class="social-icon one" href="#" aria-label="Social network one"></a>
      <a class="social-icon two" href="#" aria-label="Social network two"></a>
    </div>
  </main>

  <footer class="site-footer">© 2015 VLN Sports. All Rights Reserved</footer>
</div>
</body>
</html>
```